Medical Learning Web Design Project

The web site will be a site for medical students. It is aimed at providing a collaborative place for students to study, learn, question each other and challenge each other with learning. The site needs to have a section on the page that is for the content and this needs to be relatively clean and clinical. The surrounding elements will be informative (for the statistics, challenge etc). There will also be a slide-out screen that allows for the social/friend elements of the site.

The colour scheme needs to be clean and clinical where appropriate, but also engaging and exciting for the social/competitive elements.
Updates

Just for clarity: The site isn't expected to be 'coded' ... it is just the layered PSD files that I need.

Also, with regards to the navigation buttons ... they will never ALL be present at the same time so don't feel the need to design all on one page, but creativity around allowing few or many on a page will be an advantage ...

Thanks

Hi,

Please note that the image uploaded has been done as a wireframe by the developers. I am looking for a more creative and engaging way of presenting that content ...

Thanks

Hi all

Thank you all for the designs so far ...!

Please have a look at the new uploaded file, I am also looking not just for a 'templated home page' but also some different layouts that are represented in these wireframes. If the various layouts represented can be condensed down into 1 or 2 page templates with appropriate colour schemes to capture the type of content on the page (as already mentioned ... social .. competitive ... learning), then that will help me live the concepts better too! The friends tab for instance I have envisaged as a slider covering the screen and then sliding back when complete ... but let me see what creativity you can give to this ...!

Many thanks

Reason: Just allowing for final tweaks ...

Target Market(s)

Medical Students

Industry/Entity Type

Medical

Requirements
Must have
• - Not cluttered appearance
- Dynamic navigation (ie. site will be developed to only show relevant navigation buttons on each page ...)
- Navigation buttons (need to be individual buttons) will be: 'Home', 'Take the tour', 'What your peers say', 'Subscriptions', 'Free Signup', 'Contact us', 'Moderation', 'Statistics', 'Competition', 'Answer Questions', 'Post Questions', 'My profile', 'Friends'
- Please also ensure it is engaging for social elements and competitive elements (perhaps slightly different design for pages focussed on each element)
- Please also ensure that there is a masculine design and feminine design that has continuity for the site but depending on gender the design can be tailored to be more appealing (that means perhaps male social design, male competitive design, female social design, female competitive design ... without loosing continuity through the site).
- Photoshop PSD format
- Pixel perfect at least 1000 pixels wide (but the design needs to allow for various monitor sizes (only desktop or laptops ... not tablets or smart phones)

```html
<!DOCTYPE html>
<html lang="en">
<head>
<meta charset="utf-8">
<title>Clinora – The Medical Peer Review</title>
<link href="https://fonts.googleapis.com/css2?family=Arimo:ital,wght@0,400;0,700;1,400&family=Open+Sans:wght@400;600&display=swap" rel="stylesheet">
<style>
:root{
  --page:#ffffff;
  --band:#e9e9e9;
  --ink:#333333;
  --muted:#666666;
  --brand-green:#6aa93a;
  --nav-top:#a6dc78;
  --nav-bottom:#74bf3c;
  --nav-ink:#2f5216;
  --orange:#f4a31b;
  --login-top:#ffe17a;
  --login-bottom:#f5b92c;
  --teal-top:#8fe0e0;
  --teal-bottom:#48bcc4;
  --blue-top:#8fd3f2;
  --blue-bottom:#4aaed9;
  --feed-blue:#3a86b5;
  --link:#2a6aa8;
  --line:#d8d8d8;
  --video:#1e1e1e;
}
*{box-sizing:border-box;margin:0;padding:0}
html,body{width:909px;height:1200px;overflow:hidden;background:var(--page)}
body{position:relative;font-family:"Arimo",Arial,sans-serif;color:var(--ink);font-size:11px}
.abs{position:absolute}

/* top strip */
.web-strip{left:0;top:0;width:909px;height:29px;background:var(--band)}
.web-strip .label{left:513px;top:8px;font-size:10px;color:var(--ink)}
.social-icons{left:604px;top:4px;display:flex;gap:8px}
.social-icons span{width:21px;height:21px;border-radius:4px;display:block}

/* header */
.brand{left:100px;top:50px}
.brand .name{font-size:29px;font-weight:700;color:var(--brand-green);letter-spacing:-0.5px;line-height:1}
.brand .tag{font-size:9.5px;color:var(--ink);margin-top:1px}
.quote{left:236px;top:52px;width:230px;text-align:right;font-size:10px;font-style:italic;line-height:13px;color:var(--ink);white-space:nowrap}
.login label{position:absolute;font-size:10px;color:var(--ink)}
.login .field{position:absolute;height:19px;border:1px solid #bbb;background:#fff}
.login .btn{left:756px;top:63px;width:47px;height:20px;border-radius:10px;border:1px solid #d99a18;background:linear-gradient(var(--login-top),var(--login-bottom));font-size:10px;text-align:center;line-height:18px;color:#4a3200}
.login .check{left:516px;top:88px;width:11px;height:11px;border:1px solid #aaa;background:#fff}
.login .keep{left:532px;top:88px;font-size:10px}
.login .forgot{left:637px;top:88px;font-size:10px;text-decoration:underline;color:var(--ink)}

/* navigation */
.main-nav{left:0;top:125px;width:909px;height:24px}
.main-nav a{position:absolute;top:0;height:22px;border-radius:5px 5px 0 0;background:linear-gradient(var(--nav-top),var(--nav-bottom));color:var(--nav-ink);font-size:11px;text-align:center;line-height:22px;text-decoration:none;text-transform:uppercase}
.nav-rule{left:77px;top:147px;width:758px;height:3px;background:#d4d4d4}

/* slider */
.hero{left:100px;top:176px;width:707px;height:265px;border:1px solid var(--line);background:#fff}
.hero h1{position:absolute;left:50px;top:41px;font-size:15px;font-weight:700;color:var(--orange)}
.hero ul{position:absolute;left:69px;top:79px;list-style:none;font-size:11px;line-height:25.3px;color:var(--ink)}
.hero .art{position:absolute;left:366px;top:24px;width:300px;height:213px;border-radius:50%;background:radial-gradient(ellipse at center,#dfe7ea 0%,#eef2f3 55%,#ffffff 72%)}
.hero .arrow{position:absolute;top:115px;width:34px;height:34px;border-radius:50%;background:#e6e6e6}
.hero .arrow svg{position:absolute;left:11px;top:10px}
.dots{left:418px;top:448px;display:flex;gap:4px}
.dots span{width:10px;height:10px;border-radius:50%;background:#ddd;border:1px solid #c8c8c8}

/* video */
.section-title{left:112px;top:480px;font-size:13.5px;font-weight:700;color:var(--ink)}
.video{left:112px;top:508px;width:428px;height:259px;background:var(--video)}
.video .controls{position:absolute;left:0;top:219px;width:428px;height:40px;background:linear-gradient(#f4f4f4,#d9d9d9);font-size:8px;color:#444}
.video .track{position:absolute;left:44px;top:8px;width:330px;height:4px;border-radius:2px;background:#aaa}
.video .played{position:absolute;left:0;top:0;width:160px;height:4px;border-radius:2px;background:#666}
.video .knob{position:absolute;left:152px;top:-3px;width:16px;height:10px;border-radius:3px;background:#888}
.video .ctl{position:absolute;top:24px}

/* cards */
.card{width:220px;height:296px;border:1px solid var(--line);background:#fff}
.card .head{position:absolute;left:-1px;top:-1px;width:220px;height:27px;border-radius:6px 6px 0 0;background:linear-gradient(var(--blue-top),var(--blue-bottom));color:#1f4a66;font-size:12px;line-height:27px;padding-left:12px}
.card .art{position:absolute;left:30px;top:38px;width:160px;height:162px;border-radius:8px}
.card p{position:absolute;left:16px;top:214px;width:190px;font-family:"Open Sans",Arial,sans-serif;font-size:9.2px;line-height:12px;color:var(--ink)}
.card .more{position:absolute;right:14px;top:274px;font-size:9.5px;color:var(--ink)}

/* sidebar */
.side-head{left:580px;width:227px;height:27px;border-radius:6px;background:linear-gradient(var(--teal-top),var(--teal-bottom));color:#145257;font-size:11px;line-height:27px;padding-left:11px}
.side-head svg{position:absolute;right:10px;top:10px}
.follow-row{display:flex;gap:3px;align-items:center}
.pill{height:15px;border:1px solid #b9c3d4;border-radius:3px;background:linear-gradient(#fff,#e3e7ee);font-size:8.5px;line-height:13px;padding:0 4px;color:#333;font-weight:700;white-space:nowrap}
.count{height:15px;border:1px solid #ccc;font-size:8.5px;line-height:13px;padding:0 4px;color:#333;white-space:nowrap}
.small{font-size:8.5px;color:var(--ink)}

.fb-box{left:590px;top:610px;width:213px}
.fb-box .page-thumb{position:absolute;left:0;top:3px;width:29px;height:29px;background:#c7463f}
.fb-box .page-name{position:absolute;left:38px;top:4px;font-size:11px;font-weight:700;color:var(--link)}
.fb-box .page-name span{font-weight:400;font-size:8.5px;color:#555}
.fb-rule{left:590px;top:654px;width:213px;height:1px;background:var(--line)}
.fans{left:590px;top:672px;display:grid;grid-template-columns:repeat(5,38px);column-gap:5px;row-gap:3px}
.fans figure{text-align:center;font-size:7.5px;color:#555}
.fans figure div{width:38px;height:38px;margin-bottom:5px}

.feed{left:583px;top:860px;width:224px;height:227px;background:var(--feed-blue);border-radius:3px}
.feed .top{position:absolute;left:9px;top:6px;color:#fff}
.feed .top small{display:block;font-size:8px;color:#cfe6f5}
.feed .top strong{font-size:13px}
.feed .list{position:absolute;left:6px;top:40px;width:212px;height:158px;background:#fff}
.tweet{position:absolute;left:6px;width:200px;font-size:8.8px;line-height:11px;color:var(--ink)}
.tweet .av{position:absolute;left:0;top:2px;width:20px;height:20px}
.tweet .txt{margin-left:26px}
.tweet a{color:var(--link);text-decoration:underline}
.tweet small{display:block;font-size:7px;color:#888}
.feed .foot{position:absolute;left:0;bottom:0;width:224px;height:27px;color:#fff;font-size:9.5px}

/* footer */
.site-footer{left:0;top:1129px;width:909px;height:71px;background:var(--band);text-align:center;font-size:9.5px;color:var(--ink)}
.site-footer nav{margin-top:20px}
.site-footer p{margin-top:9px}
</style>
</head>
<body>

<div class="abs web-strip">
  <span class="abs label">Clinora on the web:</span>
  <div class="abs social-icons" aria-label="Social links">
    <span style="background:#3b5a9a"></span>
    <span style="background:#3fa9dc"></span>
    <span style="background:#2f7fb3"></span>
    <span style="background:#5e7fa6"></span>
    <span style="background:#e2e2e2;border:1px solid #bbb"></span>
    <span style="background:#4fb543"></span>
    <span style="background:#4a8fd6"></span>
    <span style="background:#3a7cc6"></span>
    <span style="background:#f08a24"></span>
  </div>
</div>

<header>
  <div class="abs brand">
    <div class="name">Clinora</div>
    <div class="tag">The Medical Peer Review</div>
  </div>
  <blockquote class="abs quote">“Clinora keeps me ahead of the game,<br>constantly testing my knowledge...”<br>- Sam, doctor in training, University of Northbridge</blockquote>

  <form class="login">
    <label style="left:516px;top:51px">Username:</label>
    <span class="field" style="left:516px;top:64px;width:113px"></span>
    <label style="left:637px;top:51px">Password:</label>
    <span class="field" style="left:637px;top:64px;width:114px"></span>
    <span class="abs btn">Login</span>
    <span class="abs check"></span>
    <span class="abs keep">Keep me signed in</span>
    <span class="abs forgot">Forgot your password?</span>
  </form>
</header>

<nav class="abs main-nav">
  <a style="left:100px;width:68px">Home</a>
  <a style="left:171px;width:102px">Take a tour</a>
  <a style="left:276px;width:161px">What your peers say</a>
  <a style="left:440px;width:152px">Subscription plans</a>
  <a style="left:595px;width:102px">Free signup</a>
  <a style="left:700px;width:107px">Contact us</a>
</nav>
<div class="abs nav-rule"></div>

<section class="abs hero">
  <h1>Clinora - The Medical Peer Review</h1>
  <ul>
    <li>- Test your medical knowledge</li>
    <li>- Answer a vast array of medical questions</li>
    <li>- Earn trophies as your knowledge increases</li>
    <li>- Rate questions from peers</li>
    <li>- Ask your own questions</li>
    <li>- Link to your friends and check thier progress</li>
  </ul>
  <div class="art" role="img" aria-label="Illustration of medical professionals standing on a connected network of circles"></div>
  <span class="arrow" style="left:8px"><svg width="10" height="14" viewBox="0 0 10 14"><path d="M8 1 2 7l6 6" fill="none" stroke="#777" stroke-width="1.6"/></svg></span>
  <span class="arrow" style="left:661px"><svg width="10" height="14" viewBox="0 0 10 14"><path d="M2 1l6 6-6 6" fill="none" stroke="#777" stroke-width="1.6"/></svg></span>
</section>
<div class="abs dots"><span></span><span></span><span></span><span></span><span></span></div>

<h2 class="abs section-title">How Clinora Works</h2>
<div class="abs video">
  <svg class="abs" style="left:198px;top:89px" width="30" height="38" viewBox="0 0 30 38"><path d="M0 0 30 19 0 38z" fill="#6a6a6a"/></svg>
  <div class="controls">
    <span class="ctl" style="left:8px;top:4px">01:46</span>
    <span class="ctl" style="left:393px;top:4px">02:28</span>
    <div class="track"><div class="played"></div><div class="knob"></div></div>
    <span class="ctl" style="left:8px">❚❚ PAUSE</span>
    <span class="ctl" style="left:114px">✉ email</span>
    <span class="ctl" style="left:166px">⚲ get link</span>
    <span class="ctl" style="left:220px">◉ get code</span>
    <span class="ctl" style="left:332px">⛶</span>
    <span class="ctl" style="left:358px">◀))</span>
    <span class="ctl" style="left:383px;top:21px;border:1px solid #aaa;border-radius:3px;padding:1px 4px;background:#f6f6f6">MENU</span>
  </div>
</div>

<article class="abs card" style="left:100px;top:793px">
  <div class="head">Statistics</div>
  <div class="art" role="img" aria-label="Illustration of a colourful 3D bar chart under a magnifying glass" style="background:linear-gradient(135deg,#f0d24a,#6fb2e6 55%,#d8d8d8)"></div>
  <p>Lorem Ipsum is simply dummy text of the printing and typesetting industry. Lorem Ipsum has been the industry's standard dummy text ever since the 1500s, when an unknown printer took...</p>
  <span class="more">more....</span>
</article>

<article class="abs card" style="left:335px;top:793px">
  <div class="head">Challenge</div>
  <div class="art" role="img" aria-label="Illustration of a cartoon doctor with a stethoscope and a pointing hand" style="background:linear-gradient(135deg,#f2d3b8,#eef1f3 55%,#6c7a86)"></div>
  <p>Lorem Ipsum is simply dummy text of the printing and typesetting industry. Lorem Ipsum has been the industry's standard dummy text ever since the 1500s, when an unknown printer took...</p>
  <span class="more">more....</span>
</article>

<aside>
  <div class="abs side-head" style="top:481px">Become a fan of Clinora<svg width="9" height="7" viewBox="0 0 9 7"><path d="M0 0h9L4.5 7z" fill="#1e5e63"/></svg></div>
  <div class="abs follow-row" style="left:592px;top:520px">
    <span class="pill">■ Follow @clinora</span>
    <span class="count">520K followers</span>
  </div>
  <div class="abs follow-row" style="left:592px;top:541px">
    <span class="pill">Like</span>
    <span class="small">■ 856,735 people like this.</span>
  </div>

  <div class="abs side-head" style="top:571px">Clinora on Friendbook<svg width="9" height="7" viewBox="0 0 9 7"><path d="M0 0h9L4.5 7z" fill="#1e5e63"/></svg></div>
  <div class="abs fb-box">
    <div class="page-thumb" role="img" aria-label="Page thumbnail"></div>
    <div class="page-name">ReelPreview.net <span>on Friendbook</span></div>
    <span class="abs pill" style="left:38px;top:20px">Like</span>
  </div>
  <div class="abs fb-rule"></div>
  <div class="abs small" style="left:590px;top:659px">9,957 people like <b>ReelPreview.net</b>.</div>
  <div class="abs fans">
    <figure><div role="img" aria-label="Fan photo" style="background:#8a4a5a"></div>Arlo</figure>
    <figure><div role="img" aria-label="Fan photo" style="background:#9aa46a"></div>Perry</figure>
    <figure><div role="img" aria-label="Fan photo" style="background:#b08a6a"></div>Nico</figure>
    <figure><div role="img" aria-label="Fan photo" style="background:#6f8aa8"></div>Bram</figure>
    <figure><div role="img" aria-label="Fan photo" style="background:#3b3b3b"></div>Tomas</figure>
    <figure><div role="img" aria-label="Fan photo" style="background:#5e6a3a"></div>DJ</figure>
    <figure><div role="img" aria-label="Fan photo" style="background:#7a8a9a"></div>KaiLu</figure>
    <figure><div role="img" aria-label="Fan photo" style="background:#c05a3a"></div>Ella</figure>
    <figure><div role="img" aria-label="Fan photo" style="background:#b07a5a"></div>Rexford</figure>
    <figure><div role="img" aria-label="Fan photo" style="background:#d8b42a"></div>Adebola</figure>
  </div>
  <div class="abs small" style="left:590px;top:789px;font-size:7.5px;color:#555">■ Friendbook social plugin</div>

  <div class="abs side-head" style="top:819px">Clinora on Chirper<svg width="9" height="7" viewBox="0 0 9 7"><path d="M0 0h9L4.5 7z" fill="#1e5e63"/></svg></div>
  <div class="abs feed">
    <div class="top"><small>What's being said about</small><strong>Harborview</strong></div>
    <div class="list">
      <div class="tweet" style="top:4px"><div class="av" role="img" aria-label="User avatar" style="background:#9a7a5a"></div><div class="txt"><a>MarcoVell</a> I'm at Harbor Bean Roasters (418 Linden St, at 9th, Harborview) <a>http://clip.zz/4kq2</a><small>3 minutes ago</small></div></div>
      <div class="tweet" style="top:64px"><div class="av" role="img" aria-label="User avatar" style="background:#6a6a6a"></div><div class="txt"><a>lena_rivers</a> Trying to get some sleep before a 15 hour trip form Oslo to Harborview tomorrow. Moving to the U.S tomorrow!!!<small>3 minutes ago</small></div></div>
      <div class="tweet" style="top:124px"><div class="av" role="img" aria-label="User avatar" style="background:#8aa0b0"></div><div class="txt"><a>pkorvath</a> Crissy field in Harborview w/ friends.<small>about 1 minute ago</small></div></div>
    </div>
    <div class="foot"><span class="abs" style="left:9px;top:7px;font-weight:700">Chirper</span><span class="abs" style="left:94px;top:8px">Join the conversation</span></div>
  </div>
</aside>

<footer class="abs site-footer">
  <nav>Home &nbsp;|&nbsp; Take a tour &nbsp;|&nbsp; What your peers say &nbsp;|&nbsp; Subscription plans &nbsp;|&nbsp; Free Signup &nbsp;|&nbsp; Contact Us &nbsp;|&nbsp; Sitemap</nav>
  <p>Copyright 2012 Clinora Limited</p>
</footer>

</body>
</html>
```